flatrotate.co.uk landing page website design

Hi designers, I would like a custom designed landing page very similar to www.dwellingtrader.co.uk. It represents a happy place, sunny days and people swapping homes. I would like this done just like theres but our own design but a similar layout as theres.

I would like the 3 reasons to use us to be

Connect to thousands of other people in your area looking for a home swap

Our service is Completely free unlike most other exchange websites.

Find a exchange within 30 days!*

Thank you all,

Hi Everyone, I need the designs to represent london if possible like one of the designers has done for anyone else being in with a chance to win. Please check out the design by KR with the london look. I still like some of the others and they may win but i need to give this a try please.

Target Market(s)

Council house tenants

Coding

Coded - Design and coding required

Number of Pages Required

1 page

Requirements
Must have
• Custom designed landing page showing all the elements that www.dwellingtrader.co.uk use, The blue sky, and the land it shows with houses and people representing people swapping house. It can not be the same as them but can be similar concept with our own custom design and colour scheme ect.

please create 3 bubbles for speech from people. Please add the following quotes. "Its time we upsize"
"lets try and downsize and save money" "shall we move house?"
Would like 2 blocks of flats in a similar way dwelling trader.co.uk show the houses.
Nice to have

Should not have
• Same colour scheme as dwelling trader apart from the blue sky

```html
<!DOCTYPE html>
<html lang="en">
<head>
<meta charset="utf-8">
<title>flatrotate.co.uk – Landing Page</title>
<link href="https://fonts.googleapis.com/css2?family=Montserrat:wght@400;500;600;700;800;900&display=swap" rel="stylesheet">
<style>
:root{
  --green:#3ab54a;
  --red:#e31b23;
  --yellow:#ffe600;
  --ink:#2b2b2b;
  --brown:#4a2318;
  --teal:#044552;
  --white:#ffffff;
  --sky-top:#86bde8;
  --sky-mid:#c9e1f3;
  --sky-low:#e2eff8;
  --grass-top:#b5d23a;
  --grass-low:#7fbb2a;
}
*{margin:0;padding:0;box-sizing:border-box}
html,body{width:741px;height:1200px;overflow:hidden}
body{font-family:'Montserrat',sans-serif;background:var(--white);position:relative;color:var(--ink)}
.abs{position:absolute}

/* header */
.site-header{left:0;top:0;width:741px;height:55px;background:var(--white)}
.brand{left:94px;top:19px;display:flex;align-items:center;gap:6px;font-weight:700;font-size:15px;color:var(--ink)}
.brand-mark{width:14px;height:14px;background:var(--green);border-radius:2px}
.phone{left:563px;top:16px;display:flex;align-items:center;gap:8px;font-size:8px;font-weight:700;color:var(--ink)}
.phone-icon{width:23px;height:23px;border-radius:50%;background:var(--red);display:flex;align-items:center;justify-content:center}

/* nav */
.main-nav{left:0;top:55px;width:741px;height:23px;background:var(--green);display:flex;padding-left:93px}
.main-nav a{color:var(--white);text-decoration:none;font-size:7.5px;font-weight:700;line-height:23px;padding:0 10.5px}
.main-nav a.active{background:var(--red);padding:0 12px}

/* scene backdrop: illustrated sky, house, sun, hills, trees and buildings */
.scene{left:0;top:78px;width:741px;height:890px;
  background:linear-gradient(180deg,var(--sky-top) 0%,var(--sky-mid) 38%,var(--sky-low) 62%,var(--sky-low) 74%,var(--grass-top) 79%,#95c532 88%,var(--grass-low) 100%)}

.hero-title{left:0;top:191px;width:741px;text-align:center;color:var(--white);font-weight:800;font-size:13.6px;text-shadow:0 1px 2px rgba(0,0,0,.35)}
.cta{left:305px;top:226px;width:120px;height:29px;background:var(--red);border-radius:4px;text-align:center;color:var(--white);text-decoration:none}
.cta strong{display:block;font-size:11px;font-weight:700;line-height:13px;padding-top:5px}
.cta span{display:block;font-size:5.6px;color:var(--yellow);font-weight:500}

/* search */
.search{left:94px;top:361px;width:553px;height:102px;background:var(--red);border-radius:13px}
.search label{position:absolute;top:22px;color:var(--white);font-size:8px;font-weight:700}
.field{position:absolute;top:47px;width:109px;height:33px;background:var(--white);border-radius:4px;font-size:8px;color:#8a8a8a;padding:12px 0 0 5px}
.caret{position:absolute;right:9px;top:14px;width:0;height:0;border-left:6px solid transparent;border-right:6px solid transparent;border-top:5px solid var(--red)}
.search-btn{position:absolute;left:455px;top:39px;width:81px;height:23px;background:var(--green);border-radius:4px;color:var(--white);font-size:8px;font-weight:700;text-align:center;line-height:23px}

/* audience pills */
.pill{top:508px;width:139px;height:93px;display:flex;align-items:center;color:var(--white);font-size:8px;font-weight:700;line-height:10px}
.pill-tenant{left:212px;background:var(--green);border-radius:47px 0 0 47px;padding-left:17px;gap:13px}
.pill-landlord{left:390px;background:var(--red);border-radius:0 47px 47px 0;padding-left:9px;gap:11px}
.pill a{color:var(--white);text-align:center}

/* reasons */
.section-title{left:0;top:633px;width:741px;text-align:center;font-size:10.8px;font-weight:800;color:var(--ink);padding-right:8px}
.icon-case{left:311px;top:725px;width:64px;height:56px}
.icon-target{left:488px;top:818px;width:58px;height:58px}
.reason{font-size:8.3px;font-weight:600;line-height:10px;color:var(--ink)}
.reason.on-grass{color:#3b3b2a}
.num{font-size:7.5px;font-weight:700}

/* footer */
.site-footer{left:0;top:968px;width:741px;height:195px;background:var(--teal);color:var(--white)}
.foot-h{position:absolute;font-size:9.2px;font-weight:600}
.foot-list{position:absolute;list-style:none;font-size:6.4px;line-height:14px}
.email{position:absolute;left:303px;top:161px;font-size:6.6px}
.copyright{left:0;top:1163px;width:741px;height:37px;background:var(--red);color:var(--white);font-size:6.4px;text-align:center;line-height:37px;border-top:1px solid #b8c2c4}
</style>
</head>
<body>

<header class="site-header abs">
  <div class="brand abs"><span class="brand-mark"></span>flatrotate.co.uk</div>
  <div class="phone abs">
    <span class="phone-icon">
      <svg width="11" height="11" viewBox="0 0 24 24" fill="none" stroke="#fff" stroke-width="2.4" stroke-linecap="round" stroke-linejoin="round"><rect x="6" y="2" width="12" height="20" rx="2"/><line x1="11" y1="18" x2="13" y2="18"/></svg>
    </span>
    07700 900418
  </div>
</header>

<nav class="main-nav abs">
  <a class="active" href="#">HOME</a><a href="#">BLOG</a><a href="#">TERM OF USE</a><a href="#">PRIVACY</a><a href="#">ACCESSIBILITY</a><a href="#">ABOUT US</a><a href="#">CONTACT</a>
</nav>

<div class="scene abs" role="img" aria-label="Illustrated scene: blue sky with a bright sun, a large stone townhouse with railings, clouds, rolling green hills with a sandy path, trees, a cream terrace house and a red brick block of flats"></div>

<h1 class="hero-title abs">Happy Place, Sunny Days and People swapping Houses</h1>
<a class="cta abs" href="#"><strong>GET STARTED</strong><span>DECIDE TO SWAP HOUSE TODAY!</span></a>

<form class="search abs">
  <label style="left:13px">LOCATION</label>
  <label style="left:167px;top:21px">BEDROOMS</label>
  <label style="left:321px">MAX RENT( £ /MONTH)</label>
  <div class="field" style="left:12px">Town or Post Code</div>
  <div class="field" style="left:167px;padding-left:6px">Any<span class="caret"></span></div>
  <div class="field" style="left:321px;padding-left:6px">Any<span class="caret"></span></div>
  <div class="search-btn">SEARCH</div>
</form>

<div class="pill pill-tenant abs"><span>Are you a<br>Tenant?</span><a href="#">Click here for<br>more info</a></div>
<div class="pill pill-landlord abs"><span>Are you a<br>Landlord?</span><a href="#">Click here for<br>more info</a></div>

<h2 class="section-title abs">WHY USE FLAT ROTATE</h2>

<div class="num abs" style="left:172px;top:687px">1</div>
<p class="reason abs" style="left:172px;top:707px">Connect to Thousands of<br>other people in your area<br>loking for home swap</p>

<svg class="icon-case abs" viewBox="0 0 64 56" fill="none" stroke="#4a2318" stroke-width="1.6">
  <rect x="1" y="10" width="62" height="45" rx="3"/>
  <rect x="24" y="2" width="16" height="8" rx="2"/>
  <circle cx="32" cy="32" r="14"/>
  <text x="32" y="38" text-anchor="middle" font-family="Montserrat,sans-serif" font-size="16" font-weight="700" fill="#4a2318" stroke="none">$</text>
</svg>
<div class="num abs" style="left:285px;top:769px">2</div>
<p class="reason abs" style="left:285px;top:789px">Our service is completely<br>free &nbsp;unlike most of other<br>home exchange networks</p>

<svg class="icon-target abs" viewBox="0 0 58 58" fill="none" stroke="#4a2318" stroke-width="1.4">
  <circle cx="20" cy="38" r="19"/><circle cx="20" cy="38" r="12"/><circle cx="20" cy="38" r="5"/>
  <line x1="20" y1="38" x2="52" y2="6"/><path d="M46 4 L56 2 L54 12 Z"/>
</svg>
<div class="num abs" style="left:468px;top:866px">3</div>
<p class="reason on-grass abs" style="left:468px;top:886px">Find an exchange<br>within 30 days</p>

<footer class="site-footer abs">
  <h3 class="foot-h" style="left:92px;top:28px">QUICK NAVIGATION</h3>
  <ul class="foot-list" style="left:92px;top:49px">
    <li>HOME</li><li>CONTACT US</li><li>ABOUT US</li><li>TERM OF USE</li><li>PRIVACY POLICY</li><li>ACCESSIBILITY</li><li>COOKIES</li><li>AD PRIVACY</li><li>HELP</li>
  </ul>
  <h3 class="foot-h" style="left:307px;top:29px">HOME SWAP ADVICE</h3>
  <ul class="foot-list" style="left:307px;top:49px"><li>BLOG</li></ul>
  <h3 class="foot-h" style="left:306px;top:73px">CONNECT WITH US</h3>
  <ul class="foot-list" style="left:307px;top:93px"><li>CHATTERBOX</li></ul>
  <h3 class="foot-h" style="left:530px;top:27px">CONTACT INFORMATION</h3>
  <ul class="foot-list" style="left:530px;top:48px"><li>42 LARKFIELD ROW</li><li>BRISTOL</li><li>BS3 9QT</li><li>UNITED KINGDOM</li></ul>
  <p class="email">Email &nbsp;support@flatrotate.co.uk</p>
</footer>

<div class="copyright abs">Copyright @ 2020 FLAT ROTATE, &nbsp;&nbsp;All Right Reserved</div>

</body>
</html>
```